Business Card for Pet Food Deliver

Looking for a business card design for a start up company. We are Brisk Hound, Premium Pet Products Brought Round.

We market and are designing a website where our clients can go to and order pet food. We then deliver to a local client base. We do person to person deliver, we do not ship at this point. We are starting off with dog and cat food and treats.

Attached is our logo. We are looking for a fun yet professional design. Eye catching with color but not over the top with color. Looking for a double sided card. Contact info on the front and our logo on the back maybe. . .

I am a huge green fan. However, I am thinking I like the orange a bit more then the blue and green for dominant colors. . .

I am attaching our logo.

The file that has our slogan under has a minor change not implemented yet. The word 'Premium' should be gray to match and the word 'Delivered' should be black to match.

Target Market(s)

We are looking to service those pet owners looking for the convenience of not having to drive to a pet store to purchase their products. We are looking for those who are web savvy and purchase online.

We will also be targeting seniors in senior communities without consistent transprotation.

Industry/Entity Type

Pet

Font styles to use
Sans Serif

Colors
f37122
3176b5
acd036

Requirements
Must have
• Double sided. Logo only on one side with a bold color for the background.

Space for name, phone number, website address, mailing address.
Should not have
• No paws, delivery trucks.

```html
<!DOCTYPE html>
<html lang="en">
<head>
<meta charset="utf-8">
<title>Brisk Hound — Business Card</title>
<link rel="stylesheet" href="https://fonts.googleapis.com/css2?family=Open+Sans:wght@400;700&display=swap">
<style>
  :root {
    --page: #e9e7e4;
    --card: #060606;
    --white: #ffffff;
    --grey: #a7a7a7;
    --orange: #f37122;
    --green: #acd036;
    --blue: #3176b5;
  }
  * { box-sizing: border-box; margin: 0; padding: 0; }
  html, body {
    width: 1200px; height: 1000px; overflow: hidden;
    background: var(--page);
    font-family: "Open Sans", Arial, sans-serif;
  }
  .canvas { position: relative; width: 1200px; height: 1000px; }
  .card {
    position: absolute; left: 170px; width: 860px; height: 450px;
    background: var(--card); border-radius: 44px;
    box-shadow: 0 10px 28px rgba(0,0,0,.25);
    overflow: hidden;
  }
  .card--back { top: 30px; }
  .card--front { top: 520px; }

  /* back side: brand name */
  .brand {
    position: absolute; left: 0; right: 0; top: 0; bottom: 0;
    display: flex; align-items: center; justify-content: center; gap: 26px;
  }
  .brand__dot { width: 40px; height: 40px; border-radius: 50%; background: var(--orange); }
  .brand__name { font-size: 84px; font-weight: 400; color: var(--grey); letter-spacing: -1px; }

  /* front side: contact */
  .headline {
    position: absolute; right: 44px; top: 46px;
    font-size: 30px; font-weight: 700; color: var(--white);
  }
  .person {
    position: absolute; left: 80px; top: 150px;
    font-size: 36px; color: var(--white); white-space: nowrap;
  }
  .person__name { font-weight: 700; }
  .person__role { font-weight: 400; }
  .address { position: absolute; left: 62px; top: 270px; color: var(--white); font-size: 24px; line-height: 1.35; }
  .address__label { color: var(--green); }
  .contact {
    position: absolute; right: 44px; bottom: 38px; text-align: right;
    color: var(--white); font-size: 24px; line-height: 1.5;
  }
  .contact__row { display: flex; align-items: center; justify-content: flex-end; gap: 12px; }
  .contact__icon { width: 20px; height: 20px; }
</style>
</head>
<body>
<main class="canvas">
  <section class="card card--back" aria-label="Card back">
    <div class="brand">
      <span class="brand__dot"></span>
      <span class="brand__name">Brisk Hound</span>
    </div>
  </section>

  <section class="card card--front" aria-label="Card front">
    <p class="headline">Brisk Hound Premium Delivered</p>
    <p class="person"><span class="person__name">Daniel Hartley</span> <span class="person__role">Nutrition Specialist</span></p>
    <address class="address" style="font-style:normal">
      <span class="address__label">Address</span><br>
      482 Alder Creek Road<br>
      Fairmont, WI 53021
    </address>
    <div class="contact">
      <div class="contact__row">
        <span>555-214-83</span>
        <svg class="contact__icon" viewBox="0 0 20 20" aria-hidden="true">
          <rect x="5" y="1.5" width="10" height="17" rx="2" fill="none" stroke="#acd036" stroke-width="2"/>
          <circle cx="10" cy="15" r="1.2" fill="#acd036"/>
        </svg>
      </div>
      <div class="contact__row">
        <span>www.BriskHoundBrings.com</span>
        <svg class="contact__icon" viewBox="0 0 20 20" aria-hidden="true">
          <g fill="none" stroke="#acd036" stroke-width="1.6">
            <circle cx="10" cy="10" r="8"/>
            <ellipse cx="10" cy="10" rx="3.5" ry="8"/>
            <line x1="2" y1="10" x2="18" y2="10"/>
            <line x1="3.5" y1="6" x2="16.5" y2="6"/>
            <line x1="3.5" y1="14" x2="16.5" y2="14"/>
          </g>
        </svg>
      </div>
    </div>
  </section>
</main>
</body>
</html>
```